Stellan App | Pre-Launch Homepage

Dear designer,
Stellan is a soon to be launched innovative & free social platform for collaborative addictions quitting.
We require a design for our pre-launch homepage that will elevate our basic wireframes to the next level.
We would like the wireframes to serve as a guideline only, and not as a final version of the design. If you have cool ideas - we would appreciate your creativity!
* This is a pre-launch website for a mobile app, and as such the design must be consistent with the general style, design and atmosphere of the app (see screenshot in the shared Drive link).
* We liked the style and feel of the following website: http://plumvane.com/ - Please let's use it as a reference as well.
* The existing text in the wireframes is there just to represent a place for text. Copy will be edited by us after the design is done.
Please find the wireframes attached, and all relevant design assets and app screenshots in the following Drive shared link -
https://files.orbelink.com/open?id=7K204XqR3tPmHc8Lw2Jd61VnaGzT
Thanks,
Marcus
Industry/Entity Type
Social
Number of Pages Required
1 page
Look and feel
Each slider illustrates characteristics of the customer's brand and the style your logo design should communicate.

```html
<!DOCTYPE html>
<html lang="en">
<head>
<meta charset="utf-8">
<title>Stellan – Become a Better Version of Yourself</title>
<link href="https://fonts.googleapis.com/css2?family=Open+Sans:wght@400;600;700&display=swap" rel="stylesheet">
<style>
:root{
  --bg-dark:#15171a;
  --accent:#f2a91f;
  --text:#e6e6e6;
  --muted:#b9b9b9;
  --rule:#5a4a33;
  --green:#3aa33a;
  --panel:#111;
  --social:#2a8fe0;
}
*{margin:0;padding:0;box-sizing:border-box}
html,body{width:1200px;height:2368px;overflow:hidden}
body{
  font-family:"Open Sans",Arial,sans-serif;color:var(--text);
  background:
    radial-gradient(ellipse 700px 500px at 15% 20%, rgba(120,80,30,.45), transparent 70%),
    radial-gradient(ellipse 700px 600px at 85% 45%, rgba(30,80,80,.45), transparent 70%),
    radial-gradient(ellipse 800px 600px at 30% 75%, rgba(90,60,30,.4), transparent 70%),
    radial-gradient(ellipse 700px 500px at 80% 90%, rgba(30,60,70,.4), transparent 70%),
    var(--bg-dark);
  position:relative;
}
.abs{position:absolute}
.phone{top:18px;right:60px;font-size:15px;line-height:20px;color:var(--text);display:flex;align-items:center;gap:8px}
.brand{top:62px;left:0;width:1200px;text-align:center;font-size:72px;line-height:90px;font-weight:700;color:var(--accent);letter-spacing:1px}
.tagline{top:172px;width:1200px;text-align:center;font-size:27px;line-height:36px;font-weight:700;color:var(--accent)}
.intro{top:226px;width:1200px;text-align:center;font-size:17px;line-height:26px;color:var(--text)}
.subscribe{left:400px;width:400px;padding:14px 18px;border:1px solid #555;background:var(--panel);box-shadow:0 4px 16px rgba(0,0,0,.5)}
.subscribe p{font-size:12px;line-height:16px;color:var(--social);font-weight:600;margin-bottom:10px}
.subscribe .row{display:flex;gap:10px}
.subscribe .field{flex:1;height:24px;background:#fff;border-radius:2px;font-size:10px;line-height:14px;color:#999;padding:5px 8px}
.subscribe .btn{width:110px;height:24px;background:var(--green);color:#fff;font-size:10px;font-weight:700;text-align:center;line-height:24px;border-radius:2px}
.subscribe.light{background:#3b3b3b;border-color:#777}
.rule{left:150px;width:900px;height:1px;background:var(--rule)}
.feature{width:300px;text-align:center}
.feature h3{font-size:18px;line-height:24px;font-weight:700;margin:18px 0 8px}
.feature p{font-size:14px;line-height:20px;color:var(--muted)}
.icon-ph{display:block;margin:0 auto}
.section-title{width:1200px;text-align:center;font-size:28px;line-height:36px;font-weight:700;color:var(--accent)}
.body{font-size:14px;line-height:21px;color:var(--muted)}
.mini{display:flex;align-items:center;gap:20px;width:330px}
.mini p{font-size:14px;line-height:20px;color:var(--muted)}
.ring{flex:none;width:76px;height:76px;border:3px solid #fff;border-radius:50%;display:flex;align-items:center;justify-content:center}
.stores{top:1810px;left:0;width:1200px;display:flex;justify-content:center;gap:70px}
.store{width:90px;height:100px;border-radius:18px}
.join{top:2140px;width:1200px;text-align:center;font-size:22px;line-height:30px;font-weight:700;color:var(--accent)}
.socials{top:2192px;width:1200px;display:flex;justify-content:center;gap:10px}
.socials span{width:22px;height:22px;border-radius:50%;background:var(--social)}
.copy{top:2252px;width:1200px;text-align:center;font-size:14px;line-height:20px}
.links{top:2296px;width:1200px;text-align:center;font-size:14px;line-height:20px}
.totop{left:982px;top:2280px;width:40px;height:40px;border:2px solid #ccc;border-radius:50%;display:flex;align-items:center;justify-content:center}
</style>
</head>
<body>

<div class="abs phone">
  <svg width="16" height="16" viewBox="0 0 24 24"><circle cx="12" cy="12" r="11" fill="#fff"/><path d="M8 6c1 0 2 2 2 3s-1 1-1 2c1 2 2 3 4 4 1 0 1-1 2-1s3 1 3 2-1 3-3 3C10 19 5 14 5 9c0-2 2-3 3-3z" fill="#222"/></svg>
  040 - 5550 187
</div>

<div class="abs brand">Stellan</div>
<h1 class="abs tagline">Become a Better Version of Yourself</h1>
<p class="abs intro">Stellan is a revolutionary &amp; free social platform for collaborative<br>addictions quitting.</p>

<div class="abs subscribe" style="top:320px">
  <p>Subscribe below for the beta release and updates</p>
  <div class="row"><div class="field">Enter your email here</div><div class="btn">GET THE BETA</div></div>
</div>

<svg class="abs" style="left:588px;top:406px" width="24" height="24" viewBox="0 0 24 24"><circle cx="12" cy="12" r="10" fill="none" stroke="#777" stroke-width="1.5"/><circle cx="12" cy="12" r="4" fill="#777"/></svg>
<div class="abs rule" style="top:448px"></div>

<div class="abs feature" style="left:150px;top:512px">
  <svg class="icon-ph" width="110" height="110" role="img" aria-label="Life buoy illustration"><circle cx="55" cy="55" r="50" fill="#c0392b"/></svg>
  <h3>Never be Alone</h3>
  <p>Forget what you know - Stellan<br>makes it fun to quit.</p>
</div>
<div class="abs feature" style="left:450px;top:512px">
  <svg class="icon-ph" width="110" height="110" role="img" aria-label="Golden star illustration"><circle cx="55" cy="55" r="50" fill="#d9a422"/></svg>
  <h3>Never be Alone</h3>
  <p>Forget what you know - Stellan<br>makes it fun to quit.</p>
</div>
<div class="abs feature" style="left:750px;top:512px">
  <svg class="icon-ph" width="110" height="110" role="img" aria-label="Lion head illustration"><circle cx="55" cy="55" r="50" fill="#cfcfcf"/></svg>
  <h3>Stay Motivated</h3>
  <p>Forget what you know - Stellan<br>makes it fun to quit.</p>
</div>

<div class="abs rule" style="top:768px"></div>

<h2 class="abs section-title" style="top:788px">FUN</h2>
<svg class="abs" style="left:180px;top:834px" width="120" height="120" role="img" aria-label="Smiling emoticon illustration"><circle cx="60" cy="60" r="54" fill="none" stroke="var(--accent)" stroke-width="4"/></svg>
<div class="abs body" style="left:480px;top:840px;width:580px">
  <p>Forget what you know - Stellan makes it fun to quit. The battle between your good and bad demons comes to life in our gamified approach for managing your campaigns.</p>
  <p style="margin-top:18px">Stellan gives you the opportunity to take an active role in helping your network to smash your common addictions as a team. That's right, reconnected the recreation process into a social game.</p>
</div>

<div class="abs rule" style="top:1008px"></div>

<h2 class="abs section-title" style="top:1030px">INSPIRE</h2>
<div class="abs body" style="left:130px;top:1080px;width:520px;text-align:center">
  <p>One of the most important factors for successful quitting is the ability to stay inspired during the process.</p>
  <p style="margin-top:18px">That's why we designed Stellan as a platform where you can inspire and be inspired by a supportive network of awesome Stellan ninjas!</p>
</div>
<svg class="abs" style="left:868px;top:1054px" width="120" height="120" viewBox="0 0 120 120"><circle cx="60" cy="60" r="54" fill="none" stroke="var(--accent)" stroke-width="4"/><path d="M60 30c10 14 20 22 20 38a20 20 0 0 1-40 0c0-10 6-16 10-22 0 8 4 12 6 12 0-10 2-18 4-28z" fill="none" stroke="var(--accent)" stroke-width="4" stroke-linejoin="round"/></svg>

<div class="abs rule" style="top:1220px"></div>

<h2 class="abs section-title" style="top:1244px">Achieve</h2>
<div class="abs body" style="left:300px;top:1300px;width:600px;text-align:center">
  <p>Stellan is built as a pyramid of relationships that makes use of the Social Cognitive Theory, to provide a powerful network of positive reinforcement.</p>
  <p style="margin-top:14px">The bigger you make it the stronger you get.</p>
</div>

<div class="abs mini" style="left:190px;top:1466px"><div class="ring"><svg width="40" height="40" viewBox="0 0 40 40"><path d="M12 8h16v8a8 8 0 0 1-16 0zM20 24v6M14 32h12" fill="none" stroke="#fff" stroke-width="3"/></svg></div><p>Forget what you know - Stellan makes it fun to quit.</p></div>
<div class="abs mini" style="left:190px;top:1584px"><div class="ring"><svg width="40" height="40" viewBox="0 0 40 40"><ellipse cx="20" cy="16" rx="11" ry="13" fill="none" stroke="#fff" stroke-width="3"/><path d="M15 30h10v5H15z" fill="#fff"/></svg></div><p>Forget what you know - Stellan makes it fun to quit.</p></div>
<div class="abs mini" style="left:740px;top:1466px"><div class="ring"><svg width="40" height="40" viewBox="0 0 40 40"><path d="M12 8h16v8a8 8 0 0 1-16 0zM20 24v6M14 32h12" fill="none" stroke="#fff" stroke-width="3"/></svg></div><p>Forget what you know - Stellan makes it fun to quit.</p></div>
<div class="abs mini" style="left:740px;top:1584px"><div class="ring"><svg width="40" height="40" viewBox="0 0 40 40"><ellipse cx="20" cy="16" rx="11" ry="13" fill="none" stroke="#fff" stroke-width="3"/><path d="M15 30h10v5H15z" fill="#fff"/></svg></div><p>Forget what you know - Stellan makes it fun to quit.</p></div>

<svg class="abs" style="left:495px;top:1420px" width="210" height="210" viewBox="0 0 210 210"><circle cx="105" cy="105" r="100" fill="none" stroke="var(--accent)" stroke-width="5"/><path d="M70 60h70v34a35 35 0 0 1-70 0zM70 68H52c0 22 10 30 20 30M140 68h18c0 22-10 30-20 30" fill="none" stroke="var(--accent)" stroke-width="7" stroke-linejoin="round"/><path d="M98 128h14v16H98zM80 146h50v14H80z" fill="var(--accent)"/></svg>

<h2 class="abs section-title" style="top:1740px;font-size:24px">Coming Soon</h2>
<div class="abs stores">
  <div class="store" style="background:#3d9a6a" role="img" aria-label="App store badge"></div>
  <div class="store" style="background:#e8e8e8" role="img" aria-label="App store badge"></div>
  <div class="store" style="background:#2a8fe0" role="img" aria-label="App store badge"></div>
</div>

<div class="abs subscribe light" style="top:1990px">
  <p>Subscribe below for the beta release and updates</p>
  <div class="row"><div class="field">Enter your email here</div><div class="btn">GET THE BETA</div></div>
</div>

<h2 class="abs join">Join the revolution</h2>
<div class="abs socials"><span></span><span></span><span></span></div>
<p class="abs copy">Copyright © 2015 Stellan Ltd.</p>
<p class="abs links">Contact Us | T&amp;Cs | Privacy Policy</p>
<div class="abs totop"><svg width="16" height="16" viewBox="0 0 16 16"><path d="M8 14V3M3 8l5-5 5 5" fill="none" stroke="#ccc" stroke-width="2"/></svg></div>

</body>
</html>
```